Postcard Design

A house cleaning business. Focus on time saving and stress free. Free estimates. Want it to state that we can make your home sparkle or shine. I have been using the colors purple and black in the logo which I will attach.

Reason: I need a few more days to decide on this. Thank you

Industry/Entity Type

House

Colors
886aae
6b449b

Requirements
Must have
• website www.tidwellhavenhomes.us
phone # 555-390-6172

```html
<!DOCTYPE html>
<html lang="en">
<head>
<meta charset="utf-8">
<title>Tidwell Haven Cleaning Company – Flyer</title>
<link rel="stylesheet" href="https://fonts.googleapis.com/css2?family=Roboto+Condensed:ital,wght@0,400;0,700;1,700&family=Archivo:ital,wght@0,700;0,800;1,900&display=swap">
<style>
  :root {
    --purple: #886aae;
    --purple-deep: #6b449b;
    --magenta: #e2137f;
    --cyan: #1b9fe0;
    --ink: #1a1a1a;
    --paper: #ffffff;
    --backdrop: #5f5f5f;
  }
  * { margin: 0; padding: 0; box-sizing: border-box; }
  html, body { width: 962px; height: 1200px; overflow: hidden; }
  body { background: var(--backdrop); font-family: "Roboto Condensed", Arial, sans-serif; }

  .flyer {
    position: absolute; left: 82px; top: 85px;
    width: 798px; height: 1030px;
    background: var(--paper); overflow: hidden;
  }
  .flyer__shapes { position: absolute; inset: 0; }

  .headline {
    position: absolute; left: 28px; top: 80px;
    font-family: "Roboto Condensed", Arial, sans-serif; font-weight: 700;
    color: var(--paper); font-size: 96px; line-height: 0.86;
    transform: rotate(-15.5deg); transform-origin: left top;
    letter-spacing: -1px;
  }
  .headline__mark {
    position: absolute; left: 425px; top: -30px;
    font-family: "Archivo", Arial, sans-serif; font-weight: 800;
    font-size: 200px; line-height: 1; color: var(--paper);
    transform: rotate(8deg);
  }

  .badge {
    position: absolute; left: 586px; top: 0;
    width: 210px; height: 210px; border-radius: 50%;
    background: var(--magenta); border: 6px solid var(--paper);
    display: flex; align-items: center; justify-content: center;
  }
  .badge__text {
    font-family: "Roboto Condensed", Arial, sans-serif; font-weight: 700;
    color: var(--paper); font-size: 32px; line-height: 1; text-align: center;
    transform: rotate(12deg);
  }

  .call {
    position: absolute; right: 60px; top: 228px;
    font-family: "Roboto Condensed", Arial, sans-serif; font-weight: 700;
    color: var(--cyan); font-size: 44px; line-height: 1.04; text-align: right;
  }

  .photo {
    position: absolute; left: 150px; top: 320px; width: 648px; height: 470px;
    background: radial-gradient(ellipse at 50% 55%, #3aa9d6 0%, #7cc3e0 24%, #e8eef2 50%, rgba(255,255,255,0) 70%);
  }

  .services {
    position: absolute; left: 40px; top: 434px; list-style: none;
    font-size: 21px; line-height: 28.5px; color: var(--ink);
  }
  .services li::before {
    content: ""; display: inline-block; margin-right: 8px;
    border-left: 10px solid var(--purple-deep);
    border-top: 7px solid transparent; border-bottom: 7px solid transparent;
    vertical-align: -1px;
  }

  .pitch {
    position: absolute; left: 38px; top: 702px;
    font-family: "Archivo", Arial, sans-serif; font-style: italic; font-weight: 900;
    color: var(--magenta); font-size: 23px; line-height: 29px;
    text-shadow: 2px 0 #fff, -2px 0 #fff, 0 2px #fff, 0 -2px #fff;
  }

  .contact { position: absolute; left: 36px; top: 862px; }
  .contact__phone {
    font-family: "Archivo", Arial, sans-serif; font-weight: 800;
    color: var(--purple); font-size: 47px; line-height: 1;
    display: flex; align-items: center; gap: 4px;
  }
  .contact__line {
    font-family: "Archivo", Arial, sans-serif; font-weight: 700;
    color: var(--cyan); font-size: 21px; margin-top: 10px;
    display: flex; align-items: center; gap: 12px;
  }
  .contact__line::before { content: ""; width: 11px; height: 11px; background: var(--purple); }
  .contact__line--first { margin-top: 18px; }
  .tagline {
    font-family: "Archivo", Arial, sans-serif; font-weight: 800;
    color: var(--purple); font-size: 24px; margin-top: 12px;
  }

  .brand {
    position: absolute; left: 545px; top: 880px; width: 235px;
    font-family: "Roboto Condensed", Arial, sans-serif; font-weight: 700;
    color: var(--purple-deep); font-size: 28px; line-height: 1.1; text-align: center;
  }
</style>
</head>
<body>
<main class="flyer">
  <svg class="flyer__shapes" width="798" height="1030" viewBox="0 0 798 1030" aria-hidden="true">
    <polygon points="0,0 798,0 798,100 398,180 0,325" fill="var(--purple)"/>
    <polygon points="398,180 798,100 798,118 398,194" fill="var(--ink)"/>
    <path d="M0,800 C180,830 300,770 480,770 C620,770 720,800 798,820 L798,1030 L0,1030 Z" fill="var(--purple)"/>
    <path d="M0,848 C200,845 320,800 480,800 C620,800 720,828 798,845 L798,1030 L0,1030 Z" fill="var(--paper)"/>
  </svg>

  <div class="photo" role="img" aria-label="Smiling cleaner in a blue t-shirt holding a plunger, spray bottle, toilet brush, scrub brush and duster"></div>

  <h1 class="headline">TIRED OF<br>CLEANING</h1>
  <span class="headline__mark" aria-hidden="true">?</span>

  <div class="badge"><p class="badge__text">INSURED<br>AND<br>BONDED</p></div>

  <h2 class="call">CALL TIDWELL HAVEN<br>CLEANING SERVICES</h2>

  <ul class="services">
    <li>Mop/Sweep</li>
    <li>Vaccum</li>
    <li>Bathrooms</li>
    <li>Wash Walls</li>
    <li>Baseboards</li>
    <li>Blinds</li>
    <li>Windows</li>
    <li>Dusting</li>
    <li>Much More!</li>
  </ul>

  <p class="pitch">TIDWELL HAVEN CLEANING COMPANY<br>OFFERS OLD FASHION, HIGH-QUALITY<br>HOME CLEANING SERVICES.</p>

  <section class="contact">
    <p class="contact__phone">
      <svg width="16" height="40" viewBox="0 0 16 40" aria-hidden="true">
        <path d="M12,2 C4,6 2,14 2,20 C2,26 4,34 12,38 L14,32 C9,30 8,25 8,20 C8,15 9,10 14,8 Z" fill="var(--purple)"/>
      </svg>
      555-390-6172
    </p>
    <p class="contact__line contact__line--first">www.tidwellhavenhomes.us</p>
    <p class="contact__line">hello@tidwellhavenhomes.us</p>
    <p class="tagline">WE CAN MAKE YOUR HOUSE SPARKLE!</p>
  </section>

  <p class="brand">Tidwell Haven<br>Cleaning Company</p>
</main>
</body>
</html>
```